Business Card Design Project

I need a new business card design for my building/development company: Ridgewell Constructions.

We specialise in small sub-divisions, multi-story developments and new house builds.
We handle the whole process from concept stage right throught to a fully developed property.
Updates

Project Deadline Extended
Reason: Need a couple of extra days to decide as there are so many amazing designs

Target Market(s)

people looking to develop their property and need help. New property buyers

Industry/Entity Type

House

Requirements
Must have
• My logo on both sides:
Side 1: Logo taking up whole side as per old card but with a color/style change.

Side 2: Contact page: include logo but the rest just surprise me!

All contact details will be: (and need to be changable for each employee) I'll inform you of specifics before printing.

Name Surname
Position ie. Managing director
M: insert mobile
E: insert email
P.O. Box 518, Elmhurst, Vic, 3145
www.ridgewellconstructions.com.au

Nice to have
• Colors i'd like: (not necessarily all but this is the basic idea)

Black, blue, grey, silver, white

```html
<!DOCTYPE html>
<html lang="en">
<head>
<meta charset="utf-8">
<title>Ridgewell Constructions – Business Card</title>
<link rel="stylesheet" href="https://fonts.googleapis.com/css2?family=Arimo:wght@400;700&display=swap">
<style>
  :root {
    --page-bg: #e9e9e9;
    --card-top: #2e2e2e;
    --card-bottom: #1b1b1b;
    --brand-blue: #1e8fd8;
    --text-white: #f2f2f2;
    --text-grey: #c9c9c9;
    --text-muted: #8c8c8c;
    --divider: #9a9a9a;
  }
  * { box-sizing: border-box; margin: 0; padding: 0; }
  html, body {
    width: 1200px; height: 1200px; overflow: hidden;
    background: var(--page-bg);
    font-family: "Arimo", Arial, sans-serif;
  }
  .sheet {
    width: 1200px; height: 1200px;
    display: flex; flex-direction: column; align-items: center; justify-content: center;
    gap: 50px;
  }
  .card {
    position: relative;
    width: 920px; height: 525px;
    background: linear-gradient(160deg, var(--card-top), var(--card-bottom));
    box-shadow: 0 12px 30px rgba(0,0,0,.35);
    overflow: hidden;
  }

  /* Front: contact side */
  .brand-block {
    position: absolute; left: 70px; top: 220px; width: 380px;
  }
  .brand-name {
    display: flex; align-items: center; gap: 12px;
    color: var(--brand-blue); font-size: 34px; font-weight: 700; line-height: 1.1;
  }
  .brand-mark {
    width: 22px; height: 22px; background: var(--brand-blue); flex: none;
  }
  .brand-tagline {
    margin-top: 8px; margin-left: 34px;
    color: var(--text-white); font-size: 17px; letter-spacing: .3px;
  }
  .divider {
    position: absolute; left: 470px; top: 90px; width: 1px; height: 300px;
    background: linear-gradient(to bottom, transparent, var(--divider) 25%, var(--divider) 75%, transparent);
  }
  .contact {
    position: absolute; left: 505px; top: 90px; right: 30px;
  }
  .person-name { color: var(--brand-blue); font-size: 34px; font-weight: 400; }
  .person-role { color: var(--text-grey); font-size: 20px; margin-top: 4px; }
  .details { list-style: none; margin-top: 48px; color: var(--text-grey); font-size: 17px; }
  .details li { display: flex; align-items: flex-start; gap: 10px; line-height: 1.3; }
  .details li + li { margin-top: 4px; }
  .details .address { margin-bottom: 14px; }
  .icon { width: 14px; height: 14px; flex: none; margin-top: 3px; fill: var(--brand-blue); }

  /* Back: brand side */
  .card-back { display: flex; flex-direction: column; align-items: center; justify-content: center; }
  .back-brand {
    display: flex; align-items: center; gap: 16px;
    color: var(--brand-blue); font-size: 44px; font-weight: 700;
  }
  .back-brand .brand-mark { width: 30px; height: 30px; }
  .back-web {
    margin-top: 90px;
    color: var(--text-muted); font-size: 24px; font-weight: 700; letter-spacing: 5px;
  }
</style>
</head>
<body>
<main class="sheet">
  <section class="card card-front" aria-label="Business card front">
    <div class="brand-block">
      <div class="brand-name"><span class="brand-mark"></span>Ridgewell Constructions</div>
      <div class="brand-tagline">renovation-construction-development</div>
    </div>
    <div class="divider"></div>
    <div class="contact">
      <h1 class="person-name">Marcus Hale</h1>
      <p class="person-role">Managing Director</p>
      <ul class="details">
        <li class="address">
          <svg class="icon" viewBox="0 0 16 16"><path d="M8 1 1 8h2v7h4v-4h2v4h4V8h2z"/></svg>
          <span>P.O. Box 518,<br>Elmhurst, Vic, 3145</span>
        </li>
        <li>
          <svg class="icon" viewBox="0 0 16 16"><path d="M1 6c0-2 3-3 7-3s7 1 7 3v1h-3V5.5H4V7H1zM3 8h10l1 6H2z"/></svg>
          <span>08 5524 3390</span>
        </li>
        <li>
          <svg class="icon" viewBox="0 0 16 16"><path d="M4 1h8v14H4zM5.5 3v8h5V3z"/></svg>
          <span>041 2965 307</span>
        </li>
        <li>
          <svg class="icon" viewBox="0 0 16 16"><path d="M1 3h14v1L8 9 1 4zM1 5.5l7 5 7-5V13H1z"/></svg>
          <span>marcus@ridgewellconstructions.com.au</span>
        </li>
        <li>
          <svg class="icon" viewBox="0 0 16 16"><circle cx="8" cy="8" r="6.5" fill="none" stroke="#1e8fd8" stroke-width="1.5"/><path d="M1.5 8h13M8 1.5c-3 3-3 10 0 13M8 1.5c3 3 3 10 0 13" fill="none" stroke="#1e8fd8" stroke-width="1.2"/></svg>
          <span>www.ridgewellconstructions.com.au</span>
        </li>
      </ul>
    </div>
  </section>

  <section class="card card-back" aria-label="Business card back">
    <div class="back-brand"><span class="brand-mark"></span>Ridgewell Constructions</div>
    <div class="back-web">www.ridgewellconstructions.com.au</div>
  </section>
</main>
</body>
</html>
```